Business Card Upgrade

I have designed our business card using our new logo. I think it needs imporovements. We used to have two cards for our business. One card was for our software business, and the other was for our consulting business. We are now in the process of combining our websites, marketing, name, and a new logo.

Our goal is to have a really sharp professional logo. One reason I designed the card the way I did was that our Titles are sometimes long, and by separating the person's name and title, it shows up very well and the title can be adjusted no matter how long it is. Sometimes the title can be 4 or 5 words or more.

We really like our logo on black as it shows up very nice. Our PMS colors are as follows: 368C and 459C.

The Designer that will be working with us will need to deliver the following:

The front and back of the Business Card Design will need to be delivered in a high quality JPEG, and
The front and back of the Business Card Design in Illustrator Format .ai
Any fonts will need to be sent to us if they are not standard and are required to open the Illustrator file correctly.

To help us get a good idea of the card with a title, please use the title: " Director of Software Development "

NOTE: The chosen designer will be selected to design our new letterhead within 2 weeks from the closing of this contest.

To help us make sure the card design works with longer titles, please use the followign job title on the card:  

"Director of Software and Product Development"

 

ALL DESIGNERS:

1. I appreciate the different angles you are showing the cards, but please be sure and always show the direct view, so I can see the layout and what the person I hand the card will see.

2. Please do not use white.  Please use off white as I don't care for white cards and they get dirty easy and do not represent the designs well.

Dear Designers,

Please provide samples straight one as a viewer of the card will see.  Some of the angles that are presented make it impossible to tell how everything fits, and sometimes even makes areas look skewed. So, please provide a straight sample view.

Pinnacle 400 company executives such as Vice Presidents, and Directors

Software

• Professional looking Card.

Our customers are Directors, Vice Presidents, and Presidents of companies as large as Pinnacle 400 companies. The card needs to get attention wile still looking professional.

Delivery of the finished product in Illustrator Format with any fonts needed to edit the text or open the file.

The card will be a heavy stock with a soft touch coating for that silk feel.

```html
<!DOCTYPE html>
<html lang="en">
<head>
<meta charset="utf-8">
<title>Business Card – Meridian Trade Group</title>
<link rel="stylesheet" href="https://fonts.googleapis.com/css2?family=Mulish:wght@400;500;800&display=swap">
<style>
  :root {
    --page: #ffffff;
    --ink: #000000;
    --sand: #e2cf89;
    --heading: #e3d08e;
    --brand-green: #5aa00a;
  }
  * { margin: 0; padding: 0; box-sizing: border-box; }
  html, body {
    width: 1200px; height: 1000px; overflow: hidden;
    background: var(--page);
    font-family: "Mulish", sans-serif;
    color: var(--ink);
  }
  .canvas { position: relative; width: 1200px; height: 1000px; }
  .page-title {
    position: absolute; top: 48px; left: 0; width: 100%;
    text-align: center; font-size: 44px; font-weight: 400;
    color: var(--heading);
  }
  .card { position: absolute; background: var(--sand); overflow: hidden; }
  .card svg.card-band { position: absolute; inset: 0; display: block; }
  .card--landscape { left: 12px; top: 157px; width: 722px; height: 416px; }
  .card--portrait { left: 768px; top: 158px; width: 416px; height: 720px; }

  .wordmark {
    position: absolute; text-align: center;
    color: var(--brand-green); font-weight: 800;
    text-transform: uppercase; letter-spacing: 2px; line-height: 1.05;
    font-size: 30px;
  }
  .card--landscape .wordmark { left: 211px; top: 62px; width: 300px; }
  .card--portrait .wordmark { left: 58px; top: 104px; width: 300px; }

  .person-name { position: absolute; font-size: 38px; font-weight: 400; line-height: 1; }
  .person-title { position: absolute; font-size: 21px; font-weight: 500; line-height: 1.2; }
  .contact { position: absolute; font-size: 20px; line-height: 26px; font-weight: 400; list-style: none; }

  .card--landscape .person-name { left: 22px; top: 196px; }
  .card--landscape .person-title { left: 22px; top: 235px; white-space: nowrap; }
  .card--landscape .contact { right: 18px; top: 264px; text-align: right; }

  .card--portrait .person-name { left: 26px; top: 352px; font-size: 36px; }
  .card--portrait .person-title { left: 26px; top: 389px; width: 360px; }
  .card--portrait .contact { left: 26px; top: 542px; }
</style>
</head>
<body>
<main class="canvas">
  <h1 class="page-title">Sample Design</h1>

  <section class="card card--landscape" aria-label="Business card, landscape">
    <svg class="card-band" viewBox="0 0 722 416" aria-hidden="true">
      <path d="M0 0 H722 V215 C640 226 560 224 470 212 C360 196 250 172 130 172 C70 173 30 179 0 188 Z" fill="var(--ink)"/>
    </svg>
    <div class="wordmark">Meridian<br>Trade Group</div>
    <p class="person-name">Dale Whitcomb</p>
    <p class="person-title">Director of Software and Product Development</p>
    <ul class="contact">
      <li>1480 Cedar Point Road</li>
      <li>Fairhope, AL 36532</li>
      <li>251.555.0148 (Direct)</li>
      <li>dwhitcomb@meridiantg.com</li>
    </ul>
  </section>

  <section class="card card--portrait" aria-label="Business card, portrait">
    <svg class="card-band" viewBox="0 0 416 720" aria-hidden="true">
      <path d="M0 0 H416 V317 C350 313 280 302 210 291 C160 284 115 284 80 287 C40 290 15 292 0 295 Z" fill="var(--ink)"/>
    </svg>
    <div class="wordmark">Meridian<br>Trade Group</div>
    <p class="person-name">Dale Whitcomb</p>
    <p class="person-title">Director of Software and Product Development</p>
    <ul class="contact">
      <li>1480 Cedar Point Road</li>
      <li>Fairhope, AL 36532</li>
      <li>251.555.0148 (Direct)</li>
      <li>dwhitcomb@meridiantg.com</li>
    </ul>
  </section>
</main>
</body>
</html>
```